Promotion material for corporate wellness firm.

I am looking to have a flyer designed that gives some background on the company offerings for corporate wellness. I have attached the content and logo files I would like included and a photo of Mae but if there are other relevant nutrition related photos we would be open to have those included. We are looking for professional but a little light.

Target Market(s)

corporate officers.

Industry/Entity Type

It Company

```html
<!DOCTYPE html>
<html lang="en">
<head>
<meta charset="utf-8">
<title>Mae Ashford Wellness – Corporate Wellness Flyer</title>
<link href="https://fonts.googleapis.com/css2?family=Raleway:wght@300;400;600;700;800&display=swap" rel="stylesheet">
<style>
  :root{
    --backdrop:#9d9d9d;
    --paper:#ffffff;
    --lime:#a3c23a;
    --ink:#555555;
    --ink-dark:#1e1e1e;
    --panel:#e9e9ea;
    --logo-grey:#6d6d6d;
    --photo-warm:#d6cdc1;
    --photo-deep:#b9ad9d;
    --produce-light:#dfe6cc;
    --produce-warm:#ecdcca;
  }
  *{box-sizing:border-box;margin:0;padding:0}
  html,body{width:1200px;height:1200px;overflow:hidden;background:var(--backdrop)}
  body{position:relative;font-family:'Raleway',sans-serif;color:var(--ink)}
  .page{position:absolute;top:250px;width:525px;height:680px;background:var(--paper);
        box-shadow:0 2px 6px rgba(0,0,0,.25);overflow:hidden}
  .page--front{left:60px}
  .page--back{left:604px}

  /* front */
  .hero{position:absolute;left:23px;top:22px;width:502px;height:334px;
        border-top-left-radius:60px;
        background:linear-gradient(160deg,var(--photo-warm) 0%,var(--photo-deep) 100%)}
  .hero__headline{position:absolute;left:31px;top:204px;color:#fff;font-weight:400;
        font-size:32px;line-height:32px;letter-spacing:.2px}
  .hero__headline strong{font-weight:800}

  .credentials{position:absolute;left:54px;top:356px;width:471px;height:112px;background:var(--lime);
        border-bottom-left-radius:40px;text-align:right;padding:16px 41px 0 20px;color:var(--ink-dark)}
  .credentials h2{font-weight:300;font-size:17px;color:#fff;margin-bottom:6px}
  .credentials p{font-size:8.2px;line-height:10px;margin-bottom:6px;font-weight:400}

  .side-label{position:absolute;writing-mode:vertical-rl;transform:rotate(180deg);
        color:var(--lime);font-weight:400;font-size:12.5px;line-height:13px}
  .blurb{position:absolute;font-size:8.4px;line-height:12.9px;font-weight:400;color:#333}

  .brand{position:absolute;display:flex;flex-direction:column;align-items:center;
        color:var(--logo-grey);font-weight:600;text-align:center}
  .brand__dot{border-radius:50%;background:var(--lime)}
  .brand__name{letter-spacing:1px;text-transform:uppercase}

  .footer-note{position:absolute;left:34px;bottom:35px;font-size:8.2px;font-weight:700;color:var(--ink-dark)}

  /* back */
  .promise{position:absolute;left:0;top:38px;width:356px;height:84px;background:var(--lime);
        border-bottom-right-radius:40px;color:#fff;font-weight:300;font-size:15.2px;line-height:17.6px;
        padding:18px 10px 0 70px}
  .services-panel{position:absolute;left:24px;top:139px;width:477px;height:284px;background:var(--panel);
        border-top-left-radius:70px}
  .col{position:absolute;width:124px;font-size:7.9px;line-height:12.8px;color:#555}
  .col h3{font-size:8px;font-weight:700;color:var(--ink-dark);line-height:12.8px}
  .col p{margin-bottom:6px}
  .produce{position:absolute;left:360px;top:338px;width:165px;height:116px;border-radius:10px;
        background:linear-gradient(135deg,var(--produce-light),var(--produce-warm))}
</style>
</head>
<body>

<section class="page page--front">
  <div class="hero" role="img" aria-label="Photo area: nutritionist standing at a kitchen counter with fresh fruit and vegetables"></div>
  <h1 class="hero__headline">you <strong>can</strong> live<br>a healthier life</h1>

  <div class="credentials">
    <h2>Credentials and education</h2>
    <p>BS in Human Nutrition and Exercise and Fitness; Lakeshore State University</p>
    <p>Dietetic Residency, MBA in Healthcare Administration; Northfield College, Maple Grove</p>
    <p>Member of the Guild of Nutrition Practitioners, Food Business Network, Dietitians in Media<br>and the Healthy Weight Practice Circle</p>
  </div>

  <div class="side-label" style="left:32px;top:486px;height:134px">Special interest<br>in corporate wellness</div>
  <p class="blurb" style="left:66px;top:490px;width:118px">I enjoy partnering with organizations who believe in health and wellness. I provide programs, tools and coaching that help employees identify and reach their goals. When employees are healthier, they're happier, more productive and have fewer sick days. Everybody benefits.</p>

  <div class="side-label" style="left:205px;top:510px;height:110px">The perfect client</div>
  <p class="blurb" style="left:226px;top:513px;width:120px">My clients are all different. People looking to lose weight, people looking to gain weight, diabetics, athletes, and so on. The one thing that they all have in common? They're truly engaged and motivated. That's what makes it work.</p>

  <div class="brand" style="left:372px;top:522px;width:124px">
    <span class="brand__dot" style="width:16px;height:16px;margin-bottom:10px"></span>
    <span class="brand__name" style="font-size:17px;line-height:20px">Mae Ashford</span>
    <span class="brand__name" style="font-size:17px;line-height:20px">Wellness</span>
  </div>

  <p class="footer-note">WebUs, nihilis, ses factuus, cononen aturnis obuludere et, unula nique acios aut gratimovit; Catquo aus, nices</p>
</section>

<section class="page page--back">
  <p class="promise">Whether it's working with individuals or large companies, the goal is the same: helping people live healthier lives.</p>

  <div class="services-panel"></div>
  <div class="side-label" style="left:57px;top:222px;height:176px">Corporate wellness services</div>

  <div class="col" style="left:78px;top:166px">
    <h3>Initial Consultation</h3>
    <p>60-minute consultation with employees, including a full nutrition assessment to understand their health history, current eating habits and goals for moving forward. Employees receive a personalized plan with strategies and tools for success. Consults are held in person, over the phone or via video messaging.</p>
    <h3>Follow-up Consultation</h3>
    <p>30-minute consultation with employees to evaluate progress toward goals, provide guidance, and to develop new</p>
  </div>
  <div class="col" style="left:210px;top:166px">
    <p>strategies if needed. Consults are held in person, over the phone or via video messaging.</p>
    <h3>Workplace Events</h3>
    <p>Coordination of workplace challenges, wellness screenings, lifestyle management programs or other engaging health events that are fun and inspire employees to stay on track toward reaching their goals.</p>
    <h3>Group Nutrition Presentations</h3>
    <p>Group speaking events or lunch-and-learns to educate employees about nutrition,</p>
  </div>
  <div class="col" style="left:342px;top:166px">
    <p>health and wellness. Popular topics include: Meal Planning Made Easy, Healthy Holiday Eating, Stress Management, Eating Well on the Road, and Dining Out.</p>
    <h3>Cooking Demonstrations</h3>
    <p>Live cooking demonstrations where employees learn how to cook delicious meals and snacks that are aligned with their dietary goals.</p>
  </div>
  <div class="produce" role="img" aria-label="Photo area: fresh vegetables, berries and leafy greens"></div>

  <div class="side-label" style="left:57px;top:452px;height:116px">Individual services</div>
  <div class="col" style="left:78px;top:455px">
    <h3>Initial Consultation</h3>
    <p>60-minute consultation, including a full nutrition assessment to understand client's health history, current eating patterns, and goals for moving forward. Client receives a personalized plan with strategies and tools for success. Consults are held in person, over the phone or via video messaging.</p>
  </div>
  <div class="col" style="left:210px;top:455px">
    <h3>Follow-up Consultations</h3>
    <p>30-minute consultation with clients to evaluate progress toward goals, provide guidance, and to develop new strategies if needed. Consults are held in person, over the phone or via video messaging.</p>
  </div>
  <div class="col" style="left:342px;top:455px">
    <h3>Grocery Store Tours</h3>
    <p>60-minute guided tour of the store, providing education about a variety of healthy foods, how to read and understand nutrition labels and claims, and meal-planning tips.</p>
  </div>

  <div class="brand" style="left:418px;top:562px;width:80px">
    <span class="brand__dot" style="width:9px;height:9px;margin-bottom:6px"></span>
    <span class="brand__name" style="font-size:9.5px;line-height:11px">Mae Ashford</span>
    <span class="brand__name" style="font-size:9.5px;line-height:11px">Wellness</span>
  </div>

  <p class="footer-note" style="left:57px">WebUs, nihilis, ses factuus, cononen aturnis obuludere et, unula nique acios aut gratimovit; Catquo aus</p>
</section>

</body>
</html>
```